I need new business cards for my webb agency.

We need front AND backside.

Front:
Name, Title, company name, www, email, adress, phone 1, skype,

Back:
Logo + We will use promo text about what we do i.e. Web design, Search engine marketing, Advertisements & Web analytics

We want to look like a young and creative web agency. Business card should match our logo and colors. Please new this is a new logo enclosed which we are not using anywhere yet.

We will print on solid quality paper.

www.plumvantix.com

Marrowfield Suites 10 th fl.
42/16 Tarnawell Soi 8
Bangkok 10110
Thailand
+66 (0) 2-487-6031

```html
<!DOCTYPE html>
<html lang="en">
<head>
<meta charset="utf-8">
<title>Plumvantix business cards</title>
<link rel="stylesheet" href="https://fonts.googleapis.com/css2?family=Montserrat:wght@400;600;700&display=swap">
<style>
  :root {
    --bg: #2a2a2c;
    --paper: #f3f3f3;
    --brown: #2e1a12;
    --orange: #f28a1c;
    --ink: #3a3a3a;
    --muted: #6d6d6d;
  }
  * { margin: 0; padding: 0; box-sizing: border-box; }
  html, body { width: 1200px; height: 900px; overflow: hidden; }
  body {
    background: var(--bg);
    font-family: "Montserrat", sans-serif;
    position: relative;
  }
  .card {
    position: absolute;
    left: 240px;
    width: 720px;
    height: 400px;
    background: var(--paper);
    overflow: hidden;
  }
  .card--front { top: 35px; }
  .card--back { top: 465px; }
  .card-shapes { position: absolute; inset: 0; }

  .brand { display: flex; align-items: center; gap: 12px; }
  .brand-dot { width: 40px; height: 40px; border-radius: 50%; background: var(--orange); }
  .brand-name { font-weight: 700; color: var(--brown); letter-spacing: 1px; font-size: 24px; }

  .front-content { position: absolute; left: 48px; top: 40px; width: 500px; }
  .person-name { margin-top: 26px; font-size: 22px; font-weight: 600; letter-spacing: 3px; color: var(--ink); }
  .person-title { margin-top: 4px; font-size: 12px; font-weight: 600; letter-spacing: 2px; color: var(--orange); }
  .contact-grid {
    margin-top: 28px;
    display: grid;
    grid-template-columns: 172px 128px 168px;
    column-gap: 16px;
    row-gap: 14px;
  }
  .contact-item { border-left: 2px solid var(--orange); padding-left: 10px; }
  .contact-label { font-size: 10px; font-weight: 700; letter-spacing: 1.5px; color: var(--orange); text-transform: uppercase; }
  .contact-value { font-size: 10px; line-height: 1.45; color: var(--muted); white-space: nowrap; }

  .back-content { position: absolute; left: 300px; top: 70px; }
  .back-content .brand-dot { width: 54px; height: 54px; }
  .back-content .brand-name { font-size: 34px; }
  .tagline { margin-top: 16px; max-width: 340px; font-size: 11px; line-height: 1.5; color: var(--muted); letter-spacing: .5px; }
  .services-title { margin-top: 12px; font-size: 11px; font-weight: 700; letter-spacing: 1.5px; color: var(--ink); text-transform: uppercase; }
  .services { list-style: none; margin-top: 10px; }
  .services li {
    border-left: 2px solid var(--orange);
    padding-left: 10px;
    margin-bottom: 8px;
    font-size: 11px;
    font-weight: 600;
    letter-spacing: 1.5px;
    color: var(--ink);
    text-transform: uppercase;
  }
</style>
</head>
<body>

<section class="card card--front" aria-label="Business card front">
  <svg class="card-shapes" viewBox="0 0 720 400" aria-hidden="true">
    <polygon points="612,0 720,0 720,400 668,400" fill="var(--brown)"/>
    <polygon points="586,0 612,0 668,400 642,400" fill="var(--orange)"/>
    <polygon points="350,400 652,334 660,400" fill="var(--brown)"/>
    <polygon points="296,400 648,318 652,342 360,400" fill="var(--orange)"/>
  </svg>
  <div class="front-content">
    <div class="brand">
      <span class="brand-dot"></span>
      <span class="brand-name">PLUMVANTIX</span>
    </div>
    <p class="person-name">TEODOR LINDQVIST</p>
    <p class="person-title">CO-FOUNDER</p>
    <div class="contact-grid">
      <div class="contact-item">
        <p class="contact-label">Address</p>
        <p class="contact-value">Marrowfield Suites 10th fl.<br>42/16 Tarnawell Soi 8<br>Bangkok 10110, Thailand</p>
      </div>
      <div class="contact-item">
        <p class="contact-label">Phone</p>
        <p class="contact-value">+66 (0) 2-487-6031</p>
      </div>
      <div class="contact-item">
        <p class="contact-label">Website</p>
        <p class="contact-value">www.plumvantix.com</p>
      </div>
      <div></div>
      <div class="contact-item">
        <p class="contact-label">Skype</p>
        <p class="contact-value">plumvantix.teodor</p>
      </div>
      <div class="contact-item">
        <p class="contact-label">Email</p>
        <p class="contact-value">teodor@plumvantix.com</p>
      </div>
    </div>
  </div>
</section>

<section class="card card--back" aria-label="Business card back">
  <svg class="card-shapes" viewBox="0 0 720 400" aria-hidden="true">
    <polygon points="0,0 300,0 120,400 0,400" fill="var(--brown)"/>
    <polygon points="268,0 300,0 120,400 88,400" fill="var(--orange)"/>
    <polygon points="0,60 300,0 330,0 0,92" fill="var(--orange)"/>
    <polygon points="720,290 720,400 160,400" fill="var(--brown)"/>
    <polygon points="720,290 720,316 220,400 160,400" fill="var(--orange)"/>
  </svg>
  <div class="back-content">
    <div class="brand">
      <span class="brand-dot"></span>
      <span class="brand-name">PLUMVANTIX</span>
    </div>
    <p class="tagline">Plumvantix is a Bangkok based web agency of high international standards.</p>
    <p class="services-title">Our services:</p>
    <ul class="services">
      <li>Web design</li>
      <li>Web development</li>
      <li>Search engine marketing</li>
      <li>Advertisements &amp; web analytics</li>
    </ul>
  </div>
</section>

</body>
</html>
```